Kelvora Template

Hi Guys,

I have just completed a logo design with Vantelo Works and I am very happy with what I have seen so far. Next I would like to create a template for the site that will be skinned into a DNN skin.

Our goal with Kelvora is to create a site were people can register and buy a e-commerce site from us. The site needs to match the logo color scheme and entice people to register. The site needs to be clear on what they are receiving and make sure that the registration process is easily accessible. our target market is the Joe Soup's that want to create an online presence and sell their products.

I'm excited to see what you guys are going to come up with.

Regards

Willem

Hi all,

Thank you for your inputs, It was hard to choose a template as I feel that so many of them where so good.

Well done.

Regards

Willem Badenhorst

```html
<!DOCTYPE html>
<html lang="en">
<head>
<meta charset="utf-8">
<title>Kelvora</title>
<link href="https://fonts.googleapis.com/css2?family=Ubuntu:wght@400;500;700&family=Vollkorn:wght@700&display=swap" rel="stylesheet">
<style>
:root{
  --blue-dark:#15598f;
  --blue:#1f6aa5;
  --blue-light:#4f9ccb;
  --orange:#f47a20;
  --orange-light:#f89a3e;
  --green:#8dc63f;
  --green-dark:#74b22a;
  --text:#444;
  --muted:#666;
  --line:#dcdcdc;
  --footer:#3c3c3c;
  --footer-bottom:#353535;
  --footer-text:#d8d8d8;
}
*{margin:0;padding:0;box-sizing:border-box}
html,body{width:960px;height:1200px;overflow:hidden}
body{position:relative;background:#fff;font-family:"Ubuntu",sans-serif;color:var(--text)}
a{color:inherit;text-decoration:none}

/* header */
.site-header{position:absolute;left:0;top:0;width:960px;height:139px;
  background:radial-gradient(ellipse 420px 160px at 480px 10px,var(--blue-light),var(--blue) 60%,var(--blue-dark))}
.util-links{position:absolute;left:581px;top:15px;font-size:9px;color:#e4f0f8;letter-spacing:.2px}
.util-links span{margin:0 4px}
.search{position:absolute;left:744px;top:11px;width:112px;height:21px;background:#fff;border-radius:3px;border:1px solid #cfd9e2}
.search svg{position:absolute;right:4px;top:3px}
.cart{position:absolute;left:736px;top:61px;display:flex;align-items:center;gap:8px;color:#fff;font-size:10px}
.cart b{font-weight:500}
.main-nav{position:absolute;top:97px;height:42px;background:linear-gradient(var(--orange-light),var(--orange));display:flex;border-radius:4px 4px 0 0}
.main-nav.left{left:104px;width:260px}
.main-nav.right{left:598px;width:258px}
.main-nav a{color:#fff;font-size:11.5px;font-weight:500;line-height:42px;padding:0 17px;border-right:1px solid rgba(255,255,255,.25)}
.main-nav a:last-child{border-right:0}
.brand-clip{position:absolute;left:350px;top:30px;width:260px;height:118px;overflow:hidden}
.brand-dome{position:absolute;left:10px;top:8px;width:240px;height:240px;border-radius:50%;background:linear-gradient(#fff 40%,#e9eef2)}
.brand{position:absolute;left:383px;top:94px;width:200px;display:flex;align-items:center;justify-content:center;gap:7px}
.brand .mark{width:16px;height:16px;background:var(--orange);flex:none}
.brand .name{font-size:30px;font-weight:700;color:var(--blue-dark);line-height:1}

/* hero */
.hero{position:absolute;left:104px;top:150px;width:752px;height:323px;border:1px solid var(--line);padding:2px;background:#fff}
.hero-photo{width:100%;height:100%;background:linear-gradient(90deg,#e9823a 0%,#f0a56a 25%,#e8dcc8 45%,#fbf7f2 62%,#fff 75%)}
.hero-copy{position:absolute;left:464px;top:70px;width:274px}
.hero-copy h1{font-size:27px;font-weight:500;color:var(--blue-dark);line-height:25px}
.hero-copy p{margin-top:8px;font-size:13px;font-weight:500;line-height:22px;color:#3a3a3a}
.btn-register{position:absolute;left:464px;top:212px;width:145px;height:36px;border-radius:3px;background:linear-gradient(#9fd64b,var(--green-dark));color:#1f3a0a;font-size:15px;font-weight:500;text-align:center;line-height:36px}
.slider-dots{position:absolute;left:669px;top:297px;display:flex;gap:4px}
.slider-dots i{width:12px;height:12px;border-radius:50%;background:#8fb6d1}
.slider-dots i.active{background:var(--blue-dark)}

/* featured */
.featured-bar{position:absolute;left:104px;top:489px;width:752px;height:38px;border-radius:3px;background:linear-gradient(var(--blue),var(--blue-dark));color:#fff}
.featured-bar h2{position:absolute;left:6px;top:10px;font-size:15px;font-weight:500}
.sort-label{position:absolute;left:474px;top:13px;font-size:10px}
.sort-select{position:absolute;left:574px;top:9px;width:168px;height:19px;background:#fff;border:1px solid #ccc;color:#999;font-size:9.5px;line-height:17px;padding-left:7px}
.sort-select svg{position:absolute;right:5px;top:3px}

.product{position:absolute;width:176px;border:1px solid var(--line);background:radial-gradient(ellipse at 50% 30%,#fff 30%,#efefef)}
.product.tall{height:259px}
.product.short{height:195px}
.product h3{position:absolute;left:13px;font-size:12px;font-weight:500;color:var(--blue-dark)}
.product p{position:absolute;left:13px;width:152px;font-size:9px;line-height:14px;color:#555}
.product .shot{position:absolute;left:50%;transform:translateX(-50%);border-radius:6px}
.product .price{position:absolute;left:15px;font-family:"Vollkorn",serif;font-weight:700;font-size:19px;color:var(--orange)}
.product .add{position:absolute;left:89px;width:72px;height:26px;border-radius:3px;background:linear-gradient(#a5d84f,var(--green));color:#fff;font-size:11px;font-weight:500;text-align:center;line-height:26px}
.tall h3{top:20px}.tall p{top:38px}.tall .shot{top:77px;width:86px;height:134px}
.tall .price{top:223px}.tall .add{top:224px}
.short .shot{top:10px;width:96px;height:110px}.short h3{top:124px}.short p{top:144px}
.short .price{top:162px}.short .add{top:163px}
.can-soup{background:linear-gradient(#9a2a22,#c44a30 50%,#d86a3a)}
.can-vegetable{background:linear-gradient(90deg,#8a8a8a,#d8d8d8 30%,#b84d32 55%,#c9a045 75%,#9a9a9a)}
.box-pumpkin{background:linear-gradient(#d66a2a,#e88a3a 40%,#c4501e)}
.box-cream{background:linear-gradient(#fafafa,#e8ead8 50%,#c9b77e)}

/* footer */
.site-footer{position:absolute;left:0;top:1025px;width:960px;height:175px;background:var(--footer);color:var(--footer-text)}
.footer-col{position:absolute;top:19px;font-size:9px;line-height:16px}
.footer-col h4{font-size:12px;font-weight:500;color:var(--orange);line-height:16px;margin-bottom:1px}
.footer-col b{color:#fff;font-weight:500}
.social{display:flex;gap:6px;margin-top:3px;margin-bottom:9px}
.social span,.payments span{display:flex;align-items:center;gap:3px;font-size:8px;color:#fff}
.social span i{width:7px;height:7px;background:#6f8fb8;display:block}
.payments{display:flex;gap:4px;margin-top:4px}
.payments span{background:#fff;color:var(--blue-dark);font-size:9px;font-weight:500;padding:0 6px;height:20px;border-radius:2px}
.footer-bottom{position:absolute;left:0;top:128px;width:960px;height:47px;background:var(--footer-bottom);border-top:1px solid #4a4a4a;text-align:center;font-size:9px;line-height:46px;color:#cfcfcf}
</style>
</head>
<body>

<header class="site-header">
  <nav class="util-links"><a href="#">My Account</a><span>|</span><a href="#">Wishlist</a><span>|</span><a href="#">Checkout</a></nav>
  <div class="search">
    <svg width="14" height="14" viewBox="0 0 14 14"><circle cx="5.5" cy="5.5" r="4" fill="none" stroke="#f47a20" stroke-width="1.8"/><line x1="8.5" y1="8.5" x2="13" y2="13" stroke="#f47a20" stroke-width="2.2" stroke-linecap="round"/></svg>
  </div>
  <div class="cart">
    <svg width="22" height="17" viewBox="0 0 22 17"><path d="M2 6h18l-2.5 10h-13z" fill="#fff"/><path d="M6 6l5-5 5 5" fill="none" stroke="#fff" stroke-width="1.6"/></svg>
    <span><b>My Cart</b> ($ <b>0</b> Items)</span>
  </div>
  <nav class="main-nav left"><a href="#">Home</a><a href="#">About Us</a><a href="#">Products</a></nav>
  <nav class="main-nav right"><a href="#">Our Store</a><a href="#">Special</a><a href="#">Contact Us</a></nav>
</header>

<div class="brand-clip"><div class="brand-dome"></div></div>
<div class="brand"><span class="mark"></span><span class="name">Kelvora</span></div>

<section class="hero">
  <div class="hero-photo" role="img" aria-label="Orange bowl of pasta and vegetable soup with a spoon, red apple behind"></div>
  <div class="hero-copy">
    <h1>Aenean Suscipit Felis Sit Amet</h1>
    <p>Maecenas pharetra orci ut enim gravida egestas pulvinar eu nulla consectetur fau-cibus nec vel tellus.</p>
  </div>
  <a class="btn-register" href="#">REGISTER NOW</a>
  <div class="slider-dots"><i class="active"></i><i></i><i></i><i></i></div>
</section>

<div class="featured-bar">
  <h2>FEATURED PRODUCTS</h2>
  <span class="sort-label">Sort by Categories:</span>
  <div class="sort-select">--Select Categories--
    <svg width="12" height="12" viewBox="0 0 12 12"><path d="M1 5l5-4 5 4z M1 7l5 4 5-4z" fill="#888"/></svg>
  </div>
</div>

<article class="product tall" style="left:104px;top:538px">
  <h3>Name goes here</h3><p>Lorem ipsum dolor sit amet, con-sect- etuer adipiscing elit,</p>
  <div class="shot can-vegetable" role="img" aria-label="Can of low sodium minestrone soup"></div>
  <span class="price">$5.99</span><a class="add" href="#">Add to Cart</a>
</article>
<article class="product short" style="left:104px;top:813px">
  <div class="shot box-cream" role="img" aria-label="Carton of cream of mushroom soup"></div>
  <h3>Name goes here</h3><p>Lorem ipsum dolor sit amet</p>
  <span class="price">$5.99</span><a class="add" href="#">Add to Cart</a>
</article>

<article class="product short" style="left:296px;top:538px">
  <div class="shot can-soup" role="img" aria-label="Jar of chunky minestrone soup"></div>
  <h3>Name goes here</h3><p>Lorem ipsum dolor sit amet</p>
  <span class="price">$8.99</span><a class="add" href="#">Add to Cart</a>
</article>
<article class="product tall" style="left:296px;top:749px">
  <h3>Name goes here</h3><p>Lorem ipsum dolor sit amet, con-sect- etuer adipiscing elit,</p>
  <div class="shot can-vegetable" role="img" aria-label="Can of low sodium minestrone soup"></div>
  <span class="price">$5.99</span><a class="add" href="#">Add to Cart</a>
</article>

<article class="product tall" style="left:488px;top:538px">
  <h3>Name goes here</h3><p>Lorem ipsum dolor sit amet, con-sect- etuer adipiscing elit,</p>
  <div class="shot box-pumpkin" role="img" aria-label="Carton of pumpkin soup"></div>
  <span class="price">$5.99</span><a class="add" href="#">Add to Cart</a>
</article>
<article class="product short" style="left:488px;top:813px">
  <div class="shot box-cream" role="img" aria-label="Carton of cream of mushroom soup"></div>
  <h3>Name goes here</h3><p>Lorem ipsum dolor sit amet</p>
  <span class="price">$5.99</span><a class="add" href="#">Add to Cart</a>
</article>

<article class="product short" style="left:680px;top:538px">
  <div class="shot can-soup" role="img" aria-label="Jar of chunky minestrone soup"></div>
  <h3>Name goes here</h3><p>Lorem ipsum dolor sit amet</p>
  <span class="price">$5.99</span><a class="add" href="#">Add to Cart</a>
</article>
<article class="product tall" style="left:680px;top:749px">
  <h3>Name goes here</h3><p>Lorem ipsum dolor sit amet, con-sect- etuer adipiscing elit,</p>
  <div class="shot box-pumpkin" role="img" aria-label="Carton of pumpkin soup"></div>
  <span class="price">$5.99</span><a class="add" href="#">Add to Cart</a>
</article>

<footer class="site-footer">
  <div class="footer-col" style="left:104px">
    <h4>Contact Information</h4>
    <b>Company Address:</b><br>Vestibulum a tempus<br>dolor. et est ut urna<br>sagittis<br><b>Phone:</b> 0123 456 7890
  </div>
  <div class="footer-col" style="left:271px">
    <h4>Site Information</h4>About Us<br>Whats New<br>Shop<br>Blog<br>Contact Us
  </div>
  <div class="footer-col" style="left:414px">
    <h4>Delivery</h4>Delivery Tracking<br>Delivery Prices<br>Shipping Policy
  </div>
  <div class="footer-col" style="left:547px">
    <h4>Services &amp; Supports</h4>Contact 24/7 Supports<br>My Account<br>Payment Methods<br>Ordering<br>Terms &amp; Conditions
  </div>
  <div class="footer-col" style="left:724px">
    <h4>Connect Us</h4>
    <div class="social"><span><i></i>Chatterly</span><span><i></i>Flitbird</span><span><i></i>Plusly</span><span><i></i>Dotpix</span></div>
    <h4>Payment Mode</h4>
    <div class="payments"><span>Paynest</span><span>Cardora</span><span>Meridex</span></div>
  </div>
  <div class="footer-bottom">Copyright © 2013 by Kelvora. All Right Reserved</div>
</footer>

</body>
</html>
```